Web Design Project for Quorvel Enterprises

Quorvel Enterprises is a small company with expertise in manufacturing, product development, global sourcing and retail. We provide sales/broker, import/export, private label and product development services to both manufacturers and retailers of food, beverage, health and beauty care and general merchandise. Would like a web site that incorporates images that inspire confidence in the areas of international trade and product development as well as convey the experience of founder and CEO in these areas.

Own web address quorvelenterprises.net and have hosting from brisk nest.com

Target Market(s)

Retail and manufacturing professionals.

Industry/Entity Type

It Company

Font styles to use
Serif
Sans Serif

Requirements
Must have
• Tabs for: Home, About Us, Services, Contact Us

```html
<!DOCTYPE html>
<html lang="en">
<head>
<meta charset="utf-8">
<title>Quorvel Enterprises</title>
<link rel="stylesheet" href="https://fonts.googleapis.com/css2?family=Open+Sans:ital,wght@0,300;0,400;0,600;0,700;1,400&family=Raleway:wght@200;300&family=Tinos:ital@1&display=swap">
<style>
  :root {
    --brand-blue: #1f47a0;
    --brand-blue-light: #6f9be0;
    --top-strip: #9cc0ee;
    --title-blue: #8fb3e3;
    --nav-grey: #9db2cf;
    --text-grey: #9a9a9a;
    --icon-grey: #b5b5b5;
    --rule: #dcdcdc;
    --hero-bg: #ececec;
    --white: #ffffff;
  }
  * { margin: 0; padding: 0; box-sizing: border-box; }
  html, body { width: 810px; height: 1200px; overflow: hidden; background: var(--white); }
  body { position: relative; font-family: "Open Sans", Arial, sans-serif; color: var(--text-grey); }
  .abs { position: absolute; }

  /* top info bar */
  .info-bar { left: 0; top: 0; width: 810px; height: 20px; background: var(--brand-blue); border-top: 4px solid var(--top-strip); }
  .info-item { position: absolute; top: 1px; font-size: 9.6px; color: var(--white); display: flex; align-items: center; gap: 5px; white-space: nowrap; }
  .social-dots { position: absolute; left: 700px; top: 3px; display: flex; gap: 3px; }
  .social-dots span { width: 9px; height: 9px; border-radius: 50%; background: var(--white); display: block; }

  /* header */
  .brand { left: 75px; top: 30px; display: flex; align-items: center; gap: 8px; }
  .brand-mark { width: 40px; height: 40px; border-radius: 50%; background: var(--brand-blue); }
  .brand-name { font-size: 21px; font-weight: 700; color: var(--brand-blue); line-height: 1; }
  .main-nav { left: 470px; top: 41px; display: flex; }
  .main-nav a { display: block; height: 22px; line-height: 20px; font-size: 10px; color: var(--nav-grey); text-decoration: none; text-align: center; }
  .main-nav .current { width: 65px; background: var(--brand-blue); color: var(--white); border-bottom: 2px solid var(--brand-blue-light); }
  .nav-services { width: 70px; margin-left: 19px; }
  .nav-about { width: 40px; margin-left: 0; }
  .nav-contact { width: 40px; margin-left: 22px; }

  /* hero */
  .hero-band { left: 0; top: 84px; width: 810px; height: 301px; background: var(--hero-bg); }
  .hero-photo { left: 76px; top: 84px; width: 660px; height: 301px;
    background: radial-gradient(circle at 52% 40%, #5fd0ff 0%, #1b6fb8 16%, #123a66 34%, transparent 55%),
                radial-gradient(circle at 98% 90%, #c0392b 0%, transparent 35%),
                linear-gradient(90deg, #1c2430 0%, #2b3a4d 40%, #223044 70%, #3a2d38 100%); }
  .hero-caption { left: 137px; top: 192px; width: 246px; height: 90px; background: rgba(70,90,110,0.6); padding: 14px 0 0 28px; overflow: hidden; }
  .hero-caption p { font-family: "Raleway", Arial, sans-serif; font-weight: 200; color: var(--white); font-size: 24px; letter-spacing: 1px; line-height: 30px; white-space: nowrap; }
  .hero-caption .small { font-size: 16px; font-weight: 300; letter-spacing: 0.8px; }
  .slider-arrow { top: 226px; width: 17px; height: 17px; border-radius: 50%; border: 1px solid #c8c8c8; }
  .slider-arrow svg { display: block; }

  /* section titles */
  .section-title { left: 0; width: 810px; text-align: center; font-size: 22px; font-weight: 700; color: var(--title-blue); letter-spacing: 0.5px; }
  .title-rule { left: 314px; width: 183px; height: 4px; border-top: 1px solid var(--rule); border-bottom: 1px solid var(--rule); }

  .body-copy { font-size: 9.6px; line-height: 12px; color: var(--text-grey); text-align: center; font-weight: 300; }
  .about-copy { font-size: 9.2px; }
  .btn { display: block; height: 21px; line-height: 19px; font-size: 9.6px; color: var(--white); background: var(--brand-blue); border-bottom: 3px solid var(--brand-blue-light); text-align: center; }

  .divider { left: 76px; top: 518px; width: 660px; height: 1px; background: var(--rule); }

  .service { top: 548px; width: 200px; text-align: center; }
  .service svg { display: block; margin: 0 auto; }
  .service h3 { margin-top: 6px; font-size: 15px; font-weight: 700; color: var(--title-blue); }
  .service p { margin-top: 7px; }
  .service .btn { width: 66px; margin: 19px auto 0; }

  /* newsletter */
  .newsletter { left: 0; top: 736px; width: 810px; height: 141px;
    background: radial-gradient(ellipse at 45% 10%, #3a3f44 0%, transparent 45%), linear-gradient(180deg, #101418 0%, #262a2e 100%); text-align: center; }
  .newsletter h2 { margin-top: 22px; font-size: 18px; font-weight: 400; color: var(--white); }
  .email-field { position: absolute; left: 239px; top: 55px; width: 332px; height: 26px; border-radius: 5px; background: rgba(150,150,150,0.75);
    font-family: "Tinos", Georgia, serif; font-style: italic; font-size: 12px; line-height: 26px; color: var(--white); }
  .newsletter .btn { position: absolute; left: 372px; top: 99px; width: 66px; }

  /* map */
  .map-area { left: 76px; top: 941px; width: 660px; height: 191px; background: linear-gradient(180deg, #a9cbf0 0%, #b9d6f3 70%, #e8eef4 100%); }

  /* footer */
  .site-footer { left: 0; top: 1141px; width: 810px; height: 59px; background: var(--brand-blue); color: var(--white); font-size: 9.6px; }
  .footer-nav { position: absolute; left: 75px; top: 10px; display: flex; gap: 13px; }
  .footer-nav a { color: var(--white); text-decoration: none; }
  .copyright { position: absolute; left: 75px; top: 40px; }
  .footer-item { position: absolute; display: flex; gap: 7px; align-items: flex-start; line-height: 11px; white-space: nowrap; }
  .site-footer .social-dots { left: 444px; top: 43px; }
  .footer-brand { position: absolute; left: 614px; top: 12px; display: flex; align-items: center; gap: 6px; }
  .footer-brand .brand-mark { width: 34px; height: 34px; background: var(--white); }
  .footer-brand .brand-name { font-size: 13px; color: var(--white); }
</style>
</head>
<body>

<div class="abs info-bar">
  <div class="info-item" style="left:222px">
    <svg width="8" height="10" viewBox="0 0 8 10"><path d="M4 0a4 4 0 0 0-4 4c0 3 4 6 4 6s4-3 4-6a4 4 0 0 0-4-4zm0 5.5A1.5 1.5 0 1 1 4 2.5a1.5 1.5 0 0 1 0 3z" fill="#fff"/></svg>
    Complete Adress Here, 1234, City
  </div>
  <div class="info-item" style="left:404px">
    <svg width="10" height="8" viewBox="0 0 10 8"><rect width="10" height="8" fill="#fff"/><path d="M0 0l5 4 5-4" stroke="#1f47a0" fill="none"/></svg>
    contact@quorvelenterprises.net
  </div>
  <div class="info-item" style="left:604px">
    <svg width="9" height="9" viewBox="0 0 10 10"><path d="M2 0l2 2.5-1.2 1.3a6 6 0 0 0 3.4 3.4L7.5 6 10 8 8.5 10C4 10 0 6 0 1.5z" fill="#fff"/></svg>
    123.456.7890
  </div>
  <div class="social-dots"><span></span><span></span><span></span></div>
</div>

<header>
  <div class="abs brand">
    <span class="brand-mark"></span>
    <span class="brand-name">Quorvel Enterprises</span>
  </div>
  <nav class="abs main-nav">
    <a class="current" href="#">Home</a>
    <a class="nav-services" href="#">Services</a>
    <a class="nav-about" href="#">About</a>
    <a class="nav-contact" href="#">Contact</a>
  </nav>
</header>

<section>
  <div class="abs hero-band"></div>
  <div class="abs hero-photo" role="img" aria-label="Businessman in a dark suit holding a glowing blue globe between his hands"></div>
  <div class="abs hero-caption">
    <p>WELCOME TO</p>
    <p class="small">QUORVEL ENTERPRISES</p>
  </div>
  <div class="abs slider-arrow" style="left:46px"><svg width="15" height="15" viewBox="0 0 15 15"><path d="M9 4L6 7.5 9 11" stroke="#c0c0c0" fill="none" stroke-width="1.4"/></svg></div>
  <div class="abs slider-arrow" style="left:748px"><svg width="15" height="15" viewBox="0 0 15 15"><path d="M6 4l3 3.5L6 11" stroke="#c0c0c0" fill="none" stroke-width="1.4"/></svg></div>
</section>

<section>
  <h2 class="abs section-title" style="top:401px">ABOUT US</h2>
  <div class="abs title-rule" style="top:426px"></div>
  <p class="abs body-copy about-copy" style="left:78px; top:443px; width:654px">"Lorem ipsum dolor sit amet, consectetur adipiscing elit, sed do eiusmod tempor incididunt ut labore et dolore magna aliqua. Ut enim ad minim veniam, quis nostrud exercitation ullamco laboris nisi ut aliquip ex ea commodo consequat. Duis aute irure dolor in reprehenderit in voluptate velit</p>
  <a class="abs btn" style="left:372px; top:480px; width:66px">More</a>
  <div class="abs divider"></div>

  <div class="abs service" style="left:70px">
    <svg width="30" height="32" viewBox="0 0 30 32"><path d="M10 2h10l-3 6h-4z" fill="var(--icon-grey)"/><ellipse cx="15" cy="20" rx="13" ry="12" fill="var(--icon-grey)"/><text x="15" y="25" font-size="14" font-weight="700" fill="#fff" text-anchor="middle" font-family="Open Sans, sans-serif">$</text></svg>
    <h3>SERVICE 1</h3>
    <p class="body-copy">"Lorem ipsum dolor sit amet, consectetur adipiscing elit, sed do eiusmod tempor incididunt ut labore et dolore magna aliqua. Ut enim ad minim veniam, quis nostrud.</p>
    <a class="btn">More</a>
  </div>
  <div class="abs service" style="left:306px">
    <svg width="36" height="32" viewBox="0 0 36 32"><rect x="2" y="20" width="6" height="11" fill="var(--icon-grey)"/><rect x="10" y="15" width="6" height="16" fill="var(--icon-grey)"/><rect x="18" y="18" width="6" height="13" fill="var(--icon-grey)"/><rect x="26" y="10" width="6" height="21" fill="var(--icon-grey)"/><path d="M3 14l8-6 7 4 12-9" stroke="var(--icon-grey)" stroke-width="2" fill="none"/><path d="M27 2h6v6" stroke="var(--icon-grey)" stroke-width="2" fill="none"/></svg>
    <h3>SERVICE 2</h3>
    <p class="body-copy">"Lorem ipsum dolor sit amet, consectetur adipiscing elit, sed do eiusmod tempor incididunt ut labore et dolore magna aliqua. Ut enim ad minim veniam, quis nostrud.</p>
    <a class="btn">More</a>
  </div>
  <div class="abs service" style="left:541px">
    <svg width="32" height="32" viewBox="0 0 32 32" fill="none" stroke="var(--icon-grey)" stroke-width="2"><circle cx="16" cy="16" r="14"/><ellipse cx="16" cy="16" rx="6" ry="14"/><path d="M2 16h28M5 9h22M5 23h22M16 2v28"/></svg>
    <h3>SERVICE 3</h3>
    <p class="body-copy">"Lorem ipsum dolor sit amet, consectetur adipiscing elit, sed do eiusmod tempor incididunt ut labore et dolore magna aliqua. Ut enim ad minim veniam, quis nostrud.</p>
    <a class="btn">More</a>
  </div>
</section>

<section class="abs newsletter" role="img" aria-label="Dark background photo of a business desk with a clock and chart sketches">
  <h2>Register your email and receive our newsletter!</h2>
  <div class="email-field">Enter Email</div>
  <a class="btn">Submit</a>
</section>

<section>
  <h2 class="abs section-title" style="top:898px">LOCATION</h2>
  <div class="abs title-rule" style="top:923px"></div>
  <div class="abs map-area" role="img" aria-label="World map showing the company location"></div>
</section>

<footer class="abs site-footer">
  <nav class="footer-nav">
    <a href="#">Home</a><a href="#">Services</a><a href="#">About</a><a href="#">Contact</a>
  </nav>
  <p class="copyright">© 2014 Quorvel Enterprises. All Rights Reserved.</p>
  <div class="footer-item" style="left:288px; top:10px">
    <svg width="8" height="10" viewBox="0 0 8 10"><path d="M4 0a4 4 0 0 0-4 4c0 3 4 6 4 6s4-3 4-6a4 4 0 0 0-4-4zm0 5.5A1.5 1.5 0 1 1 4 2.5a1.5 1.5 0 0 1 0 3z" fill="#fff"/></svg>
    <span>Complete Adress Here,<br>1234, City</span>
  </div>
  <div class="footer-item" style="left:444px; top:10px">
    <svg width="9" height="9" viewBox="0 0 10 10"><path d="M2 0l2 2.5-1.2 1.3a6 6 0 0 0 3.4 3.4L7.5 6 10 8 8.5 10C4 10 0 6 0 1.5z" fill="#fff"/></svg>
    <span>123.456.7890</span>
  </div>
  <div class="footer-item" style="left:444px; top:26px">
    <svg width="10" height="8" viewBox="0 0 10 8"><rect width="10" height="8" fill="#fff"/><path d="M0 0l5 4 5-4" stroke="#1f47a0" fill="none"/></svg>
    <span>contact@quorvelenterprises.net</span>
  </div>
  <div class="social-dots"><span></span><span></span><span></span></div>
  <div class="footer-brand">
    <span class="brand-mark"></span>
    <span class="brand-name">Quorvel Enterprises</span>
  </div>
</footer>

</body>
</html>
```